Bref créative
Clearwave Imaging
Business Cards, Letter Head, Envelopes
Professional
Dorothea Kessling, RDMS, RVT
President
41672 Bramblewood Ave., # 208
Santa Clarita, CA 91387
dorothea@clear-wave-im.com
www.clear-wave-im.com
Ultrasound Studies Performed:
Abdomen, Renal, Thyroid, Breast, Scrotal, GYN/OB/NT, Vascular: LE & UE Venous and Arterial, ABI, Carotid, Renal Artery, Vein Mapping, Hemodialysis Access Graft
We are launching our business card, letter head, envelopes and fax project.

```html
<!DOCTYPE html>
<html lang="en">
<head>
<meta charset="utf-8">
<title>Clearwave Imaging — Letterhead and Compliments Slip</title>
<link href="https://fonts.googleapis.com/css2?family=Jost:wght@400;500;600&display=swap" rel="stylesheet">
<style>
  :root {
    --backdrop: #2a5aa6;
    --paper: #ffffff;
    --brand-blue: #1f6fc4;
    --brand-deep: #0d3f8f;
    --ink: #1b2433;
    --link-blue: #2a7fd4;
  }
  * { box-sizing: border-box; margin: 0; padding: 0; }
  html, body {
    width: 1200px; height: 871px; overflow: hidden;
    background: var(--backdrop);
    font-family: "Jost", "Futura", sans-serif;
  }
  .stationery { position: relative; width: 1200px; height: 871px; }

  .sheet {
    position: absolute;
    background: var(--paper);
    box-shadow: 0 6px 18px rgba(0, 0, 0, 0.25);
    overflow: hidden;
  }
  .sheet__stripe {
    position: absolute; left: 0; top: 0; bottom: 0;
    background: linear-gradient(180deg, var(--brand-blue), var(--brand-deep));
  }

  .brand { display: flex; align-items: center; justify-content: flex-end; gap: 6px; }
  .brand__dot { border-radius: 50%; background: var(--brand-blue); flex: none; }
  .brand__name { color: var(--brand-deep); font-weight: 600; white-space: nowrap; }

  .contact { text-align: right; color: var(--ink); font-weight: 600; }
  .contact__web { color: var(--link-blue); }

  /* Letterhead */
  .letterhead { left: 65px; top: 48px; width: 427px; height: 720px; }
  .letterhead .sheet__stripe { width: 14px; }
  .letterhead .brand { position: absolute; right: 14px; top: 74px; }
  .letterhead .brand__dot { width: 14px; height: 14px; }
  .letterhead .brand__name { font-size: 22px; }
  .letterhead .contact {
    position: absolute; right: 14px; top: 150px;
    font-size: 8.5px; line-height: 1.45;
  }

  /* Compliments slip */
  .slip { left: 492px; top: 360px; width: 655px; height: 307px; }
  .slip .sheet__stripe { width: 20px; }
  .slip .brand { position: absolute; right: 22px; top: 40px; }
  .slip .brand__dot { width: 16px; height: 16px; }
  .slip .brand__name { font-size: 25px; }
  .slip .contact {
    position: absolute; right: 22px; top: 108px;
    font-size: 8px; line-height: 1.45;
  }
  .slip__greeting {
    position: absolute; right: 30px; top: 228px;
    color: var(--link-blue); font-size: 19px; font-weight: 500;
    letter-spacing: 0.3px;
  }
</style>
</head>
<body>
<main class="stationery">
  <section class="sheet letterhead" aria-label="Letterhead">
    <div class="sheet__stripe"></div>
    <div class="brand">
      <span class="brand__dot"></span>
      <span class="brand__name">Clearwave Imaging</span>
    </div>
    <address class="contact">
      41672 Bramblewood Ave., # 208<br>
      Santa Clarita, CA 91387<br>
      Telephone: 818-555-0147<br>
      Email: dorothea@clear-wave-im.com<br>
      <span class="contact__web">Website: www.clear-wave-im.com</span>
    </address>
  </section>

  <section class="sheet slip" aria-label="Compliments slip">
    <div class="sheet__stripe"></div>
    <div class="brand">
      <span class="brand__dot"></span>
      <span class="brand__name">Clearwave Imaging</span>
    </div>
    <address class="contact">
      41672 Bramblewood Ave., # 208<br>
      Santa Clarita, CA 91387<br>
      Telephone: 818-555-0147<br>
      Email: dorothea@clear-wave-im.com<br>
      <span class="contact__web">Website: www.clear-wave-im.com</span>
    </address>
    <p class="slip__greeting">with compliments</p>
  </section>
</main>
</body>
</html>
```